Business card design needed

I need a business card design for a dog walking, dog minding and dog training business. Please refer to my website for the basic company colours and fonts I'm after. Planning on a double sided card, so all information doesn't need to be on the 'front' side.
Cheers

Industry/Entity Type

Dog Training

Contact Information for Business Card

Bramble Paws - guiding hounds
Ned 0487306914
bramblepawsdemo.com.au
-walking
-holiday stays
-onsite care
-training and behavioural consultations

```html
<!DOCTYPE html>
<html lang="en">
<head>
<meta charset="utf-8">
<title>Bramble Paws – business card</title>
<link rel="stylesheet" href="https://fonts.googleapis.com/css2?family=Questrial&display=swap">
<style>
  :root {
    --page: #ffffff;
    --card-light: #f7f7f7;
    --card-dark: #2c2f31;
    --card-dark-edge: #232527;
    --orange: #f26a1b;
    --ink: #3a3a3a;
    --muted: #9a9a9a;
    --white: #ffffff;
    --photo-a: #eceae6;
    --photo-b: #d8d6d2;
    --silhouette: #3a3d3f;
  }
  * { box-sizing: border-box; margin: 0; padding: 0; }
  html, body {
    width: 1200px; height: 900px; overflow: hidden;
    background: var(--page);
    font-family: "Questrial", "Century Gothic", sans-serif;
  }
  .stage {
    position: relative; width: 1200px; height: 900px;
    display: flex; align-items: center; justify-content: center; gap: 50px;
  }
  .card {
    position: relative; width: 525px; height: 300px;
    border-radius: 22px; overflow: hidden;
    box-shadow: 0 6px 18px rgba(0,0,0,0.18);
  }

  /* Front */
  .card--front { background: var(--card-light); }
  .front__top {
    position: absolute; left: 0; top: 0; width: 100%; height: 172px;
    background: linear-gradient(180deg, #ffffff, var(--card-light));
  }
  .front__photo {
    position: absolute; right: 0; top: 0; width: 230px; height: 172px;
    background: radial-gradient(ellipse at 45% 45%, var(--photo-a), var(--photo-b) 80%, #f4f4f4);
  }
  .wordmark {
    position: absolute; left: 26px; top: 64px;
    font-size: 44px; letter-spacing: 1px; color: var(--orange); line-height: 1;
    white-space: nowrap;
  }
  .tagline {
    position: absolute; left: 128px; top: 134px;
    font-size: 19px; color: var(--ink);
  }
  .front__stripe {
    position: absolute; left: 0; top: 172px; width: 100%; height: 9px;
    background: var(--orange);
  }
  .front__band {
    position: absolute; left: 0; top: 181px; width: 100%; height: 119px;
    background: linear-gradient(180deg, var(--card-dark), var(--card-dark-edge));
  }
  .contact__name {
    position: absolute; left: 26px; top: 10px;
    font-size: 19px; color: var(--orange);
  }
  .contact__list {
    position: absolute; left: 66px; top: 34px; list-style: none;
  }
  .contact__item {
    display: flex; align-items: center; gap: 5px;
    font-size: 19px; color: var(--white); line-height: 25px;
  }
  .contact__icon { width: 17px; height: 17px; flex: none; }

  /* Back */
  .card--back {
    background: radial-gradient(ellipse at 60% 30%, #3a3d40, var(--card-dark) 60%, var(--card-dark-edge));
  }
  .services {
    position: absolute; left: 70px; right: 20px; top: 52px;
    list-style: none; text-align: center;
    font-size: 18px; color: var(--white); line-height: 23px;
  }
  .back__scene {
    position: absolute; left: 20px; top: 190px; width: 230px; height: 90px;
    border-radius: 40px;
    background: radial-gradient(ellipse at center, var(--silhouette), rgba(44,47,49,0) 72%);
  }
  .back__brand {
    position: absolute; right: 24px; top: 200px; text-align: right;
  }
  .back__wordmark {
    font-size: 38px; color: var(--orange); letter-spacing: 1px; line-height: 1; white-space: nowrap;
  }
  .back__tagline {
    margin-top: 6px; font-size: 16px; color: var(--muted);
  }
</style>
</head>
<body>
<main class="stage">

  <section class="card card--front" aria-label="Business card front">
    <div class="front__top"></div>
    <div class="front__photo" role="img" aria-label="Photo of a small white puppy with its front paws raised"></div>
    <div class="wordmark">BRAMBLE PAWS</div>
    <div class="tagline">guiding hounds</div>
    <div class="front__stripe"></div>
    <div class="front__band">
      <div class="contact__name">Ned</div>
      <ul class="contact__list">
        <li class="contact__item">
          <svg class="contact__icon" viewBox="0 0 20 20" aria-hidden="true">
            <path d="M3 7c0-3 3-4 7-4s7 1 7 4l-3 1-1-2H7L6 8z" fill="var(--orange)"/>
            <rect x="4" y="9" width="12" height="8" rx="2" fill="var(--orange)"/>
            <circle cx="10" cy="13" r="2" fill="var(--card-dark)"/>
          </svg>
          0487306914
        </li>
        <li class="contact__item">
          <svg class="contact__icon" viewBox="0 0 20 20" aria-hidden="true">
            <circle cx="10" cy="10" r="8" fill="none" stroke="var(--orange)" stroke-width="2"/>
            <ellipse cx="10" cy="10" rx="3.5" ry="8" fill="none" stroke="var(--orange)" stroke-width="1.5"/>
            <line x1="2" y1="10" x2="18" y2="10" stroke="var(--orange)" stroke-width="1.5"/>
          </svg>
          bramblepawsdemo.com.au
        </li>
        <li class="contact__item">
          <svg class="contact__icon" viewBox="0 0 20 20" aria-hidden="true">
            <rect x="2" y="4" width="16" height="12" fill="none" stroke="var(--orange)" stroke-width="2"/>
            <path d="M2 4l8 7 8-7" fill="none" stroke="var(--orange)" stroke-width="1.8"/>
          </svg>
          ned@bramblepawsdemo.com.au
        </li>
      </ul>
    </div>
  </section>

  <section class="card card--back" aria-label="Business card back">
    <ul class="services">
      <li>dog walking</li>
      <li>dog minding</li>
      <li>dog training and behavioural consultations</li>
    </ul>
    <div class="back__scene" role="img" aria-label="Faint silhouettes of dogs playing together"></div>
    <div class="back__brand">
      <div class="back__wordmark">BRAMBLE PAWS</div>
      <div class="back__tagline">guiding hounds</div>
    </div>
  </section>

</main>
</body>
</html>
```